Book Cover - For Best Selling Diet

Hi
Book cover required for a diet book being marketed to become a best seller
For best quality, image will be 2820 pixels on the shortest side and 4500 pixels on the longest side .
The book name : Bright Morning Plan
By Corinna Plett
( will add in the extra text once we see design - top and bottom subtitle )
I do not want a photo of a person on the book.
PLEASE SEE " THE 9 STEP FRAME" by Ned Galbury as an example of solid style and I also love Quiet Ledger for the font.
Branding Colours:
#F26432
#A4195C
#A7D8CC
Font that runs through our brand is : helvetica neue
This is for a book that will be marketed for #1 bestseller - So please only quality
designs that are designed in a unique style.
Thanks
Target Market(s)
Busy Working Mums, Affluent, 30+ .
Look and feel

```html
<!DOCTYPE html>
<html lang="en">
<head>
<meta charset="utf-8">
<title>Bright Morning Plan — Book Cover</title>
<link rel="stylesheet" href="https://fonts.googleapis.com/css2?family=Inter:wght@200;400&display=swap">
<style>
  :root {
    --stage: #1a1a1a;
    --brand-orange: #F26432;
    --brand-magenta: #A4195C;
    --brand-mint: #A7D8CC;
    --body-low: #B3235A;
    --title-fill: #ffffff;
    --title-stroke: #A4195C;
    --author-ink: #1f1f1f;
    --badge-gold: #D9B548;
    --badge-green: #2E5A2C;
  }
  html, body {
    margin: 0;
    padding: 0;
    width: 1000px;
    height: 1200px;
    overflow: hidden;
    background: var(--stage);
  }
  .book-cover {
    position: absolute;
    left: 222px;
    top: 157px;
    width: 555px;
    height: 885px;
    display: block;
  }
  .cover-ground { fill: var(--brand-magenta); }
  .title-line {
    font-family: "Inter", "Helvetica Neue", Arial, sans-serif;
    font-weight: 200;
    font-size: 94px;
    fill: var(--title-fill);
    stroke: var(--title-stroke);
    stroke-width: 3;
    paint-order: stroke;
    text-anchor: middle;
  }
  .author-band { fill: var(--brand-mint); stroke: var(--brand-orange); stroke-width: 2; }
  .author-name {
    font-family: "Inter", "Helvetica Neue", Arial, sans-serif;
    font-weight: 400;
    font-size: 30px;
    fill: var(--author-ink);
    text-anchor: middle;
  }
  .badge-rim { fill: var(--badge-gold); }
  .badge-core { fill: var(--badge-green); }
</style>
</head>
<body>
  <svg class="book-cover" viewBox="0 0 555 885" role="group" aria-label="Bright Morning Plan by Corinna Plett">
    <defs>
      <linearGradient id="glow-vertical" x1="0" y1="0" x2="0" y2="1">
        <stop offset="0" stop-color="var(--brand-orange)"/>
        <stop offset="1" stop-color="var(--body-low)"/>
      </linearGradient>
      <linearGradient id="glow-fade" x1="0" y1="0" x2="1" y2="0">
        <stop offset="0" stop-color="#fff" stop-opacity="0"/>
        <stop offset="0.25" stop-color="#fff" stop-opacity="1"/>
        <stop offset="0.75" stop-color="#fff" stop-opacity="1"/>
        <stop offset="1" stop-color="#fff" stop-opacity="0"/>
      </linearGradient>
      <mask id="glow-mask">
        <rect x="20" y="0" width="515" height="885" fill="url(#glow-fade)"/>
      </mask>
    </defs>

    <rect class="cover-ground" x="0" y="0" width="555" height="885"/>

    <rect class="figure-glow" x="20" y="0" width="515" height="885"
          fill="url(#glow-vertical)" mask="url(#glow-mask)"
          role="img" aria-label="Stylised figure silhouette in warm orange to rose tones"/>

    <g class="bestseller-badge" role="img" aria-label="Bestseller badge">
      <circle class="badge-rim" cx="130" cy="138" r="54"/>
      <circle class="badge-core" cx="130" cy="138" r="42"/>
    </g>

    <text class="title-line" x="277" y="352">BRIGHT</text>
    <text class="title-line" x="277" y="460">MORNING</text>
    <text class="title-line" x="277" y="568">PLAN</text>

    <rect class="author-band" x="0" y="762" width="555" height="47"/>
    <text class="author-name" x="277" y="796">Corinna Plett</text>
  </svg>
</body>
</html>
```